Business Card for a Floral & Decorating Business

I would like to take my current logo and create a better business card. I am looking for elegance as I am a florist and event decorator. My logo has multiple colour options. I like colours like green, purple, pink and orange, I think I would like a white card, open to black back ground. I want it to feel elegant and romantic. I like metallic lettering that maybe is indented in the paper, I also like glossy paper. I have a full logo already as well as a badge. I have attached both in multiple colours.m

Target Market(s)

Weddings, special events, floral customers

Industry/Entity Type

Floral and decorating

Contact Information for Business Card

Phone number, email, instagram, facebook, title, name, logo

Font styles to use
Script

Requirements
Nice to have
• Elegant

```html
<!DOCTYPE html>
<html lang="en">
<head>
<meta charset="utf-8">
<title>Maren Ashby – Business Card</title>
<link rel="stylesheet" href="https://fonts.googleapis.com/css2?family=Cinzel:wght@500&family=Arimo:wght@400&display=swap">
<style>
  :root {
    --stage: #1d1d1e;
    --card: #0b0b0b;
    --card-edge: #151515;
    --teal: #5f9c90;
    --white: #f2f2f2;
    --rule: #3a3a3a;
  }
  * { box-sizing: border-box; margin: 0; padding: 0; }
  html, body { width: 1200px; height: 900px; overflow: hidden; }
  body {
    background: var(--stage);
    display: flex;
    align-items: center;
    justify-content: center;
    gap: 40px;
    font-family: "Arimo", Arial, sans-serif;
  }
  .card {
    position: relative;
    width: 540px;
    height: 309px;
    background: radial-gradient(ellipse at 40% 40%, #141414 0%, var(--card) 70%);
    border: 1px solid var(--card-edge);
    box-shadow: 0 18px 40px rgba(0,0,0,.55);
  }
  .brand {
    display: flex;
    align-items: center;
    gap: 12px;
  }
  .brand-dot {
    width: 34px; height: 34px;
    border-radius: 50%;
    background: var(--teal);
    flex: none;
  }
  .brand-name {
    font-family: "Cinzel", Georgia, serif;
    font-weight: 500;
    font-size: 24px;
    letter-spacing: 1.5px;
    color: var(--teal);
    white-space: nowrap;
  }

  /* Front: contact side */
  .card-front .brand {
    position: absolute;
    left: 36px;
    top: 136px;
  }
  .card-front .divider {
    position: absolute;
    left: 268px;
    top: 70px;
    width: 1px;
    height: 170px;
    background: var(--rule);
  }
  .contact {
    position: absolute;
    left: 292px;
    top: 78px;
  }
  .contact-name {
    font-family: "Cinzel", Georgia, serif;
    font-weight: 500;
    font-size: 21px;
    letter-spacing: 1px;
    color: var(--teal);
    line-height: 1;
  }
  .contact-title {
    margin-top: 4px;
    font-size: 14px;
    color: var(--white);
  }
  .contact-list {
    list-style: none;
    margin-top: 30px;
  }
  .contact-list li {
    display: flex;
    align-items: center;
    gap: 8px;
    font-size: 14.5px;
    color: var(--white);
    line-height: 22px;
  }
  .contact-list svg { width: 14px; height: 14px; flex: none; }
  .contact-list .accent { color: var(--teal); }

  /* Back: logo side */
  .card-back .brand {
    position: absolute;
    left: 50%;
    top: 100px;
    transform: translateX(-50%);
  }
  .card-back .brand-name { font-size: 28px; }
  .card-back .brand-dot { width: 40px; height: 40px; }
  .social {
    position: absolute;
    left: 50%;
    top: 170px;
    transform: translateX(-50%);
    display: flex;
    align-items: center;
    gap: 8px;
    font-size: 13px;
    color: var(--white);
  }
  .social-dot {
    width: 18px; height: 18px;
    border-radius: 50%;
    background: var(--teal);
  }
  .card-back .rule {
    position: absolute;
    left: 120px;
    right: 120px;
    top: 214px;
    height: 1px;
    background: var(--rule);
  }
</style>
</head>
<body>

  <section class="card card-front" aria-label="Card front with contact details">
    <div class="brand">
      <span class="brand-dot"></span>
      <span class="brand-name">Maren Ashby</span>
    </div>
    <span class="divider"></span>
    <div class="contact">
      <p class="contact-name">ELLIOT MARSH</p>
      <p class="contact-title">Managing Director</p>
      <ul class="contact-list">
        <li>
          <svg viewBox="0 0 16 16" aria-hidden="true"><path fill="none" stroke="var(--teal)" stroke-width="1.6" d="M4 2l2 3-1.5 1.5a8 8 0 0 0 5 5L11 10l3 2-1.5 2.5C7 14 2 9 1.5 3.5z"/></svg>
          055-987 654 321
        </li>
        <li>
          <svg viewBox="0 0 16 16" aria-hidden="true"><rect x="1" y="3" width="14" height="10" fill="var(--teal)"/><path d="M1 3l7 6 7-6" fill="none" stroke="var(--card)" stroke-width="1.2"/></svg>
          hello@marenashby.com
        </li>
        <li>
          <svg viewBox="0 0 16 16" aria-hidden="true"><g fill="none" stroke="var(--teal)" stroke-width="1.3"><circle cx="8" cy="8" r="6.5"/><ellipse cx="8" cy="8" rx="3" ry="6.5"/><path d="M1.5 8h13M3 4.5h10M3 11.5h10"/></g></svg>
          <span>www.<span class="accent">marenashby</span>.com</span>
        </li>
      </ul>
    </div>
  </section>

  <section class="card card-back" aria-label="Card back with brand">
    <div class="brand">
      <span class="brand-dot"></span>
      <span class="brand-name">Maren Ashby</span>
    </div>
    <div class="social">
      <span class="social-dot"></span>
      <span>@marenashby</span>
    </div>
    <span class="rule"></span>
  </section>

</body>
</html>
```